Velbrook App Homepage Design making customers feel in control of their spend

Hi,
We need a App Homepage design with a UI similar to the attached mock up on an Quillo 4. The app is intended to put customers in control of their usage and spend on their fixed phone, broadband, mobile, gas and electricity.

Please fee free to propose improvements to the background images, icons, colours, etc.

Any questions please let me know.

Thanks
Tomasz

Target Market(s)

Consumer customers

Industry/Entity Type

Internet

Font styles to use
Sans Serif

Colors
3276b5
0255a3
85acd3
cfdeed
ffffff

Requirements
Must have
• Content in line with the guidelines in the attached mock up

```html
<!DOCTYPE html>
<html lang="en">
<head>
<meta charset="utf-8">
<title>Velbrook – Home</title>
<link rel="stylesheet" href="https://fonts.googleapis.com/css2?family=Montserrat:wght@600;700&family=Raleway:wght@200;300;400&display=swap">
<style>
  :root {
    --brand-blue: #3276b5;
    --brand-navy: #0e3a6e;
    --tab-blue: #4a95d0;
    --pill-blue: #2c7fbf;
    --electric: #2d80c0;
    --gas: #27ae60;
    --mobile: #16a085;
    --calls: #c0392b;
    --internet: #8e44ad;
    --online: #27ae60;
    --ink: #454545;
    --ink-soft: #555555;
    --rule: #a8a8a8;
    --white: #ffffff;
    --calendar: #2c7fbf;
  }
  * { margin: 0; padding: 0; box-sizing: border-box; }
  html, body { width: 675px; height: 1200px; overflow: hidden; background: var(--white); }
  .app { position: relative; width: 675px; height: 1200px; font-family: "Raleway", sans-serif; color: var(--ink); }

  .app-header { position: absolute; left: 0; top: 0; width: 675px; height: 178px; background: var(--brand-blue); box-shadow: 0 2px 4px rgba(0,0,0,.25); }
  .brand { position: absolute; left: 22px; top: 58px; display: flex; align-items: center; gap: 14px; }
  .brand-dot { width: 52px; height: 52px; border-radius: 50%; background: var(--white); }
  .brand-name { font-family: "Montserrat", sans-serif; font-weight: 600; font-size: 44px; color: var(--brand-navy); line-height: 1; }
  .status-dot { position: absolute; left: 494px; top: 74px; width: 34px; height: 34px; border-radius: 50%; background: var(--online); }
  .avatar { position: absolute; left: 543px; top: 42px; width: 98px; height: 98px; border-radius: 50%; background: radial-gradient(circle at 45% 40%, #e9d2c2, #9c7a63 70%, #5a4636); border: 3px solid var(--white); }

  .last-bill { position: absolute; left: 455px; top: 180px; width: 220px; height: 54px; }
  .last-bill svg { position: absolute; inset: 0; }
  .last-bill span { position: absolute; right: 30px; top: 9px; font-family: "Montserrat", sans-serif; font-weight: 600; font-size: 28px; color: var(--white); }

  .greeting { position: absolute; left: 0; top: 283px; width: 675px; text-align: center; }
  .greeting h1 { font-family: "Montserrat", sans-serif; font-weight: 700; font-size: 40px; color: var(--ink); line-height: 48px; }
  .greeting p { font-weight: 200; font-size: 41px; color: var(--ink-soft); line-height: 48px; }
  .divider { position: absolute; left: 0; top: 399px; width: 675px; height: 1px; background: var(--rule); }

  .services { list-style: none; }
  .service { position: absolute; right: 0; height: 68px; border-radius: 34px 0 0 34px; display: flex; align-items: center; padding-left: 24px; gap: 20px; color: var(--white); font-weight: 200; font-size: 41px; }
  .service svg { width: 36px; height: 36px; flex: none; }
  .service--electricity { left: 141px; top: 459px; background: var(--electric); }
  .service--gas { left: 66px; top: 528px; background: var(--gas); }
  .service--mobile { left: 320px; top: 597px; background: var(--mobile); }
  .service--calls { left: 265px; top: 666px; background: var(--calls); }
  .service--internet { left: 439px; top: 734px; background: var(--internet); }

  .total { position: absolute; left: 23px; top: 886px; width: 630px; height: 115px; border-radius: 58px; background: var(--pill-blue); box-shadow: 0 3px 6px rgba(0,0,0,.3); text-align: center; color: var(--white); }
  .total-amount { display: block; font-family: "Montserrat", sans-serif; font-weight: 700; font-size: 72px; line-height: 76px; margin-top: 2px; color: #eef3f8; }
  .total-label { display: block; font-weight: 200; font-size: 36px; line-height: 34px; margin-top: -6px; }

  .renewal { position: absolute; left: 136px; top: 1011px; display: flex; align-items: center; gap: 10px; }
  .calendar { position: relative; width: 101px; height: 100px; }
  .calendar svg { position: absolute; inset: 0; }
  .calendar span { position: absolute; left: 0; width: 101px; top: 38px; text-align: center; font-family: "Montserrat", sans-serif; font-weight: 600; font-size: 40px; color: #9a9a9a; }
  .renewal p { font-weight: 300; font-size: 31px; color: var(--ink); margin-top: 14px; }

  .footer-rule { position: absolute; left: 23px; top: 1145px; width: 634px; height: 1px; background: var(--rule); }
  .support { position: absolute; left: 444px; top: 1152px; display: flex; align-items: center; gap: 12px; font-weight: 400; font-size: 22px; font-variant: small-caps; color: #222; }
  .support svg { width: 46px; height: 44px; }
</style>
</head>
<body>
<main class="app">
  <header class="app-header">
    <div class="brand"><span class="brand-dot"></span><span class="brand-name">Velbrook</span></div>
    <span class="status-dot"></span>
    <div class="avatar" role="img" aria-label="Profile photo of the account holder"></div>
  </header>

  <div class="last-bill">
    <svg viewBox="0 0 220 54" width="220" height="54"><polygon points="0,0 220,0 220,54 54,54" fill="var(--tab-blue)"/></svg>
    <span>Last Bill</span>
  </div>

  <section class="greeting">
    <h1>Good Morning Maren</h1>
    <p>Welcome to Velbrook</p>
  </section>
  <div class="divider"></div>

  <ul class="services">
    <li class="service service--electricity">
      <svg viewBox="0 0 24 24"><path d="M14 2 5 14h6l-2 8 9-12h-6z" fill="#fff"/></svg>Electricity
    </li>
    <li class="service service--gas">
      <svg viewBox="0 0 24 24"><path d="M12 2c1 4 6 6 6 12a6 6 0 0 1-12 0c0-3 2-5 3-6 0 2 1 3 2 3-1-3 0-6 1-9zm0 11c-1 2-3 3-3 5a3 3 0 0 0 6 0c0-2-2-3-3-5z" fill="#fff" fill-rule="evenodd"/></svg>Gas
    </li>
    <li class="service service--mobile">
      <svg viewBox="0 0 24 24"><rect x="6.5" y="1.5" width="11" height="21" rx="1.5" fill="none" stroke="#fff" stroke-width="1.4"/><line x1="7" y1="5" x2="17" y2="5" stroke="#fff" stroke-width="1"/><line x1="7" y1="19" x2="17" y2="19" stroke="#fff" stroke-width="1"/></svg>Mobile
    </li>
    <li class="service service--calls">
      <svg viewBox="0 0 24 24"><path d="M6.6 2.5 9.5 6c.4.5.4 1.2 0 1.7L8 9.4c1.3 2.7 3.9 5.3 6.6 6.6l1.7-1.5c.5-.4 1.2-.4 1.7 0l3.5 2.9c.5.4.6 1.2.1 1.7l-2 2.2c-.7.7-1.8 1-2.8.6C9.3 19.7 4.3 14.7 2.1 9.2c-.4-1 0-2.1.6-2.8l2.2-2c.5-.5 1.3-.4 1.7.1z" fill="#fff"/></svg>Calls
    </li>
    <li class="service service--internet">
      <svg viewBox="0 0 24 24" fill="none" stroke="#fff" stroke-width="1.6"><circle cx="12" cy="12" r="10"/><ellipse cx="12" cy="12" rx="4.5" ry="10"/><line x1="2" y1="12" x2="22" y2="12"/><line x1="12" y1="2" x2="12" y2="22"/><path d="M4 6.5h16M4 17.5h16"/></svg>Internet
    </li>
  </ul>

  <section class="total">
    <span class="total-amount">£68.39</span>
    <span class="total-label">Your current total charges</span>
  </section>

  <div class="renewal">
    <div class="calendar">
      <svg viewBox="0 0 101 100" width="101" height="100">
        <rect x="3" y="10" width="95" height="87" rx="8" fill="var(--calendar)"/>
        <rect x="12" y="30" width="77" height="58" fill="#fff"/>
        <rect x="24" y="0" width="9" height="20" rx="4" fill="var(--calendar)" stroke="#fff" stroke-width="2"/>
        <rect x="68" y="0" width="9" height="20" rx="4" fill="var(--calendar)" stroke="#fff" stroke-width="2"/>
      </svg>
      <span>18</span>
    </div>
    <p>Till allowance renews</p>
  </div>

  <div class="footer-rule"></div>
  <div class="support">
    <svg viewBox="0 0 46 44" fill="none" stroke="var(--calendar)" stroke-width="4">
      <path d="M7 26V21a16 16 0 0 1 32 0v5"/>
      <rect x="4" y="22" width="8" height="13" rx="3" fill="var(--calendar)"/>
      <rect x="34" y="22" width="8" height="13" rx="3" fill="var(--calendar)"/>
      <path d="M38 35c0 5-6 7-13 7" stroke-width="3"/>
    </svg>
    <span>24/7 Support</span>
  </div>
</main>
</body>
</html>
```